Re-design of Business Card

We require a design for our business card.

Korrim is a supplier of industrial packaging specializing in plastic products. We are undergoing a rebranding to appear more corporate. We have changed our company name to korrim and have a new logo.

I have uploaded our old card design with the previous company name.
Don't copy the current design. We are looking for a new design.

Industry/Entity Type

Manufacturing

Contact Information for Business Card

please don't copy the current design. we are looking for a new design.

Font styles to use
Sans Serif

Colors

Designer to choose colors to be used in the design.

Requirements
Must have
• clean and easy to read.

```html
<!DOCTYPE html>
<html lang="en">
<head>
<meta charset="utf-8">
<title>Korrim Business Card</title>
<link href="https://fonts.googleapis.com/css2?family=PT+Sans+Narrow:wght@700&family=Source+Sans+3:wght@400;600;700&display=swap" rel="stylesheet">
<style>
  :root{
    --orange:#f4822a;
    --white:#ffffff;
    --stage:#4a4e50;
    --text-font:"Source Sans 3", Arial, sans-serif;
    --head-font:"PT Sans Narrow", "Arial Narrow", sans-serif;
  }
  html,body{margin:0;padding:0;overflow:hidden;}
  body{width:1200px;height:1050px;background:var(--stage);position:relative;font-family:var(--text-font);}
  .card{position:absolute;width:770px;height:470px;left:215px;overflow:hidden;}
  .card-front{top:36px;background:var(--white);}
  .card-back{top:540px;background:var(--orange);}
  .block{position:absolute;background:var(--orange);}
  .bar-left{left:24px;top:23px;width:92px;height:158px;}
  .bar-right{left:655px;top:23px;width:91px;height:158px;}
  .logo-frame{position:absolute;left:142px;top:21px;width:490px;height:160px;box-sizing:border-box;border:12px solid var(--orange);background:var(--white);display:flex;align-items:center;justify-content:center;}
  .logo-word{font-family:var(--text-font);font-weight:700;color:var(--orange);font-size:112px;letter-spacing:2px;line-height:1;}
  .web-band{left:24px;top:201px;width:403px;height:40px;display:flex;align-items:center;gap:12px;padding-left:12px;box-sizing:border-box;color:var(--white);font-size:23px;}
  .person{left:24px;top:260px;width:403px;height:186px;color:var(--white);}
  .label-bar{position:absolute;background:var(--white);color:var(--orange);font-family:var(--head-font);font-weight:700;display:flex;align-items:center;}
  .person .label-bar{left:12px;top:14px;width:378px;height:38px;font-size:30px;padding-left:14px;box-sizing:border-box;}
  .person .job{position:absolute;left:28px;top:58px;font-size:29px;}
  .line{position:absolute;display:flex;align-items:center;gap:12px;font-size:25px;color:var(--white);}
  .person .phone{left:26px;top:102px;}
  .person .mail{left:26px;top:142px;font-size:23px;}
  .office{left:450px;top:201px;width:296px;height:245px;}
  .office .label-bar{left:16px;top:14px;width:264px;height:40px;font-size:36px;justify-content:center;}
  .office .addr{left:30px;top:66px;}
  .office .addr-lines{position:absolute;left:30px;top:66px;font-size:25px;color:var(--white);line-height:33px;}
  .office .addr-lines span{display:block;}
  .office .tel{left:30px;top:166px;}
  .office .fax{left:30px;top:203px;}
  .icon{flex:none;display:block;}
  .back-frame{position:absolute;left:12px;top:12px;right:12px;bottom:12px;border:2px solid var(--white);}
  .services{position:absolute;left:40px;top:34px;color:var(--white);margin:0;padding:0;list-style:none;}
  .services .group{font-family:var(--head-font);font-weight:700;font-size:26px;line-height:30px;}
  .services .item{font-size:19px;line-height:25px;display:flex;align-items:center;gap:8px;}
  .services .note{font-size:19px;line-height:25px;}
  .badge{position:absolute;top:40px;width:108px;height:108px;border-radius:50%;border:4px solid var(--white);box-sizing:border-box;}
  .badge-1{left:340px;}
  .badge-2{left:468px;}
  .badge-3{left:600px;}
  .map{position:absolute;left:370px;top:178px;width:352px;height:272px;border-radius:18px;background:linear-gradient(160deg,rgba(255,255,255,.92),rgba(255,255,255,.78));}
</style>
</head>
<body>

<section class="card card-front">
  <div class="block bar-left"></div>
  <div class="logo-frame"><span class="logo-word">KORRIM</span></div>
  <div class="block bar-right"></div>

  <div class="block web-band">
    <svg class="icon" width="24" height="24" viewBox="0 0 24 24"><circle cx="12" cy="12" r="11" fill="#fff"/><g fill="none" stroke="#f4822a" stroke-width="1.3"><circle cx="12" cy="12" r="8"/><ellipse cx="12" cy="12" rx="3.5" ry="8"/><path d="M4 12h16M5.5 8h13M5.5 16h13"/></g></svg>
    <span>www.harlowpack.com.au</span>
  </div>

  <div class="block person">
    <div class="label-bar">Dana Wells</div>
    <div class="job">Machinery Sales Manager</div>
    <div class="line phone">
      <svg class="icon" width="32" height="32" viewBox="0 0 32 32"><circle cx="16" cy="16" r="15" fill="#fff"/><path d="M11 8c1.5-.8 2.5 2.5 3 4 .3 1-1.2 1.6-1 2.5.6 2 2.2 3.8 4.4 4.6.9.3 1.6-1.2 2.6-.9 1.5.5 4.6 1.6 3.8 3.1-.8 1.6-2.7 2.4-4.6 1.8C14 21.7 10.4 18 9 13.2c-.5-2 .5-4.3 2-5.2z" fill="#f4822a"/></svg>
      <span>XXXX XXX XXX</span>
    </div>
    <div class="line mail">
      <svg class="icon" width="32" height="32" viewBox="0 0 32 32"><circle cx="16" cy="16" r="15" fill="#fff"/><rect x="8" y="10.5" width="16" height="11" fill="#f4822a"/><path d="M8 10.5l8 6.5 8-6.5M8 21.5l6-5M24 21.5l-6-5" fill="none" stroke="#fff" stroke-width="1.2"/></svg>
      <span>dana@lakorrim.com.au</span>
    </div>
  </div>

  <div class="block office">
    <div class="label-bar">Head Office</div>
    <div class="addr-lines">
      <span><svg class="icon" style="display:inline-block;vertical-align:-4px;margin-right:6px" width="30" height="30" viewBox="0 0 30 30"><path d="M15 3a7 7 0 0 0-7 7c0 5 7 12 7 12s7-7 7-12a7 7 0 0 0-7-7z" fill="#fff"/><circle cx="15" cy="10" r="3" fill="#f4822a"/><ellipse cx="15" cy="25" rx="11" ry="3" fill="none" stroke="#fff" stroke-width="2"/></svg>48 Harlow St</span>
      <span>Brendale Park, Qld</span>
      <span>4500 Australia</span>
    </div>
    <div class="line tel">
      <svg class="icon" width="30" height="28" viewBox="0 0 30 28"><path d="M3 10c0-4 6-6 12-6s12 2 12 6v2h-6v-3H9v3H3z" fill="#fff"/><path d="M8 14h14l3 10H5z" fill="#fff"/><circle cx="15" cy="19" r="3" fill="#f4822a"/></svg>
      <span>1300 555 014</span>
    </div>
    <div class="line fax">
      <svg class="icon" width="30" height="28" viewBox="0 0 30 28"><rect x="8" y="2" width="14" height="8" fill="#fff"/><rect x="3" y="10" width="24" height="11" rx="2" fill="#fff"/><rect x="8" y="17" width="14" height="9" fill="#fff" stroke="#f4822a" stroke-width="1.5"/></svg>
      <span>+61 7 5550 1234</span>
    </div>
  </div>
</section>

<section class="card card-back">
  <div class="back-frame"></div>
  <ul class="services">
    <li class="group">Pallet Containment</li>
    <li class="item"><svg class="icon" width="15" height="15" viewBox="0 0 15 15"><rect x="1" y="2" width="11" height="11" fill="none" stroke="#fff" stroke-width="1.6"/><path d="M4 7l3 3 7-8" fill="none" stroke="#fff" stroke-width="2"/></svg>Strech</li>
    <li class="item"><svg class="icon" width="15" height="15" viewBox="0 0 15 15"><rect x="1" y="2" width="11" height="11" fill="none" stroke="#fff" stroke-width="1.6"/><path d="M4 7l3 3 7-8" fill="none" stroke="#fff" stroke-width="2"/></svg>Heat Shrink</li>
    <li class="item"><svg class="icon" width="15" height="15" viewBox="0 0 15 15"><rect x="1" y="2" width="11" height="11" fill="none" stroke="#fff" stroke-width="1.6"/><path d="M4 7l3 3 7-8" fill="none" stroke="#fff" stroke-width="2"/></svg>Pallet Hood</li>
    <li class="group">Flexible Packaging</li>
    <li class="item"><svg class="icon" width="15" height="15" viewBox="0 0 15 15"><rect x="1" y="2" width="11" height="11" fill="none" stroke="#fff" stroke-width="1.6"/><path d="M4 7l3 3 7-8" fill="none" stroke="#fff" stroke-width="2"/></svg>Baos &amp; Lines</li>
    <li class="item"><svg class="icon" width="15" height="15" viewBox="0 0 15 15"><rect x="1" y="2" width="11" height="11" fill="none" stroke="#fff" stroke-width="1.6"/><path d="M4 7l3 3 7-8" fill="none" stroke="#fff" stroke-width="2"/></svg>Tube</li>
    <li class="item"><svg class="icon" width="15" height="15" viewBox="0 0 15 15"><rect x="1" y="2" width="11" height="11" fill="none" stroke="#fff" stroke-width="1.6"/><path d="M4 7l3 3 7-8" fill="none" stroke="#fff" stroke-width="2"/></svg>Film &amp; Sheet</li>
    <li class="item"><svg class="icon" width="15" height="15" viewBox="0 0 15 15"><rect x="1" y="2" width="11" height="11" fill="none" stroke="#fff" stroke-width="1.6"/><path d="M4 7l3 3 7-8" fill="none" stroke="#fff" stroke-width="2"/></svg>Printed Films [12col ]</li>
    <li class="item"><svg class="icon" width="15" height="15" viewBox="0 0 15 15"><rect x="1" y="2" width="11" height="11" fill="none" stroke="#fff" stroke-width="1.6"/><path d="M4 7l3 3 7-8" fill="none" stroke="#fff" stroke-width="2"/></svg>Shrink Films</li>
    <li class="group">Pallet Wrapping Machinery</li>
    <li class="item"><svg class="icon" width="15" height="15" viewBox="0 0 15 15"><rect x="1" y="2" width="11" height="11" fill="none" stroke="#fff" stroke-width="1.6"/><path d="M4 7l3 3 7-8" fill="none" stroke="#fff" stroke-width="2"/></svg>Semi &amp; Fully Auto Lines</li>
    <li class="item"><svg class="icon" width="15" height="15" viewBox="0 0 15 15"><rect x="1" y="2" width="11" height="11" fill="none" stroke="#fff" stroke-width="1.6"/><path d="M4 7l3 3 7-8" fill="none" stroke="#fff" stroke-width="2"/></svg>Finance Options include</li>
    <li class="note">Lease, Rent and pay per wrap</li>
    <li class="group">Flexi Packaging</li>
  </ul>

  <div class="badge badge-1"></div>
  <div class="badge badge-2"></div>
  <div class="badge badge-3"></div>

  <div class="map" role="img" aria-label="Map of Australia and New Zealand marking distribution locations"></div>
</section>

</body>
</html>
```